Commercial & Industrial Electrical - Millwright Maintenance Flyer

Want to create a flyer with picture of Service Man and some of pictures and highlights on the attachment I have attached. We like to use colors of Orange-Blue -Black where possible

```html
<!DOCTYPE html>
<html lang="en">
<head>
<meta charset="utf-8">
<title>Summit Ridge Millwright Maintenance Flyer</title>
<link href="https://fonts.googleapis.com/css2?family=Montserrat:wght@600;700;800;900&family=Open+Sans:wght@400;600;700&display=swap" rel="stylesheet">
<style>
  :root {
    --orange: #f5a623;
    --orange-deep: #ee8f0b;
    --navy: #1d3f73;
    --navy-dark: #152c52;
    --black: #111111;
    --ink: #2b2b2b;
    --paper: #ffffff;
    --backdrop: #e6e6e4;
  }
  * { box-sizing: border-box; margin: 0; padding: 0; }
  html, body { width: 1200px; height: 3000px; overflow: hidden; }
  body { background: var(--backdrop); font-family: "Open Sans", Arial, sans-serif; color: var(--ink); }

  .flyer {
    position: absolute; left: 20px; top: 750px;
    width: 1160px; height: 1500px;
    background: var(--paper);
    box-shadow: 0 6px 24px rgba(0,0,0,.12);
    overflow: hidden;
  }

  /* brand */
  .brand { position: absolute; left: 48px; top: 48px; width: 330px; display: flex; align-items: center; gap: 14px; }
  .brand-mark { width: 34px; height: 34px; background: var(--black); flex: none; }
  .brand-name { font-family: "Montserrat", sans-serif; font-weight: 700; font-size: 24px; line-height: 1.2; color: var(--black); }

  /* title */
  .title { position: absolute; right: 44px; top: 58px; width: 560px; text-align: center; }
  .title-kicker { font-family: "Montserrat", sans-serif; font-weight: 800; font-size: 25px; letter-spacing: .5px; color: var(--black); }
  .title-main { font-family: "Montserrat", sans-serif; font-weight: 900; font-size: 66px; line-height: .98; color: var(--black); margin-top: 6px; }
  .title-rule { height: 6px; background: var(--black); margin-top: 12px; }

  /* badge */
  .badge {
    position: absolute; left: 300px; top: 255px; width: 190px; height: 190px; border-radius: 50%;
    background: var(--orange); display: flex; align-items: center; justify-content: center; text-align: center;
    font-family: "Montserrat", sans-serif; font-weight: 800; font-size: 19px; line-height: 1.2; color: var(--navy-dark); padding: 20px;
  }

  /* services column */
  .services { position: absolute; left: 48px; top: 480px; width: 480px; }
  .service-title { font-family: "Montserrat", sans-serif; font-weight: 800; font-size: 36px; line-height: 1.12; color: var(--navy); }
  .service-title .hours { color: var(--orange); }
  .service-copy { font-size: 15px; line-height: 1.55; margin-top: 18px; color: var(--ink); }
  .service-block + .service-block { margin-top: 48px; }

  /* industries panel */
  .industries { position: absolute; left: 580px; top: 252px; width: 540px; height: 1060px; background: var(--navy-dark); padding: 22px 22px 0; }
  .industries-head {
    background: var(--paper); text-align: center; padding: 18px 10px;
    font-family: "Montserrat", sans-serif; font-weight: 800; font-size: 30px; line-height: 1.15; color: var(--navy-dark);
  }
  .industry-grid { display: grid; grid-template-columns: 1fr 1fr; gap: 14px; margin-top: 18px; }
  .industry { position: relative; height: 164px; }
  .industry-photo { position: absolute; inset: 0; }
  .industry-label {
    position: absolute; left: 10px; right: 10px; bottom: 8px; background: var(--orange);
    font-family: "Montserrat", sans-serif; font-weight: 700; font-size: 14px; color: var(--navy-dark);
    text-align: center; padding: 6px 4px; border-radius: 3px;
  }
  .tone-a { background: linear-gradient(160deg, #b9c4cf, #6f7f90); }
  .tone-b { background: linear-gradient(160deg, #d6dadf, #8d97a3); }
  .tone-c { background: linear-gradient(160deg, #9fb0c4, #4f6278); }
  .tone-d { background: linear-gradient(160deg, #c8b79a, #7c6b52); }

  /* emergency band */
  .emergency {
    position: absolute; left: 0; top: 1330px; width: 100%; height: 58px; background: var(--orange);
    display: flex; align-items: center; justify-content: center;
    font-family: "Montserrat", sans-serif; font-weight: 800; font-size: 28px; color: var(--paper);
  }

  /* footer */
  .footer {
    position: absolute; left: 0; top: 1388px; width: 100%; height: 112px; background: var(--black);
    display: flex; justify-content: space-around; align-items: center; padding: 0 30px;
  }
  .contact { display: flex; align-items: center; gap: 12px; color: #e8e8e8; font-size: 12.5px; line-height: 1.45; }
  .contact svg { width: 34px; height: 34px; flex: none; }
</style>
</head>
<body>
<main class="flyer">

  <div class="brand">
    <span class="brand-mark"></span>
    <span class="brand-name">Summit Ridge Millwrights &amp; Maintenance</span>
  </div>

  <header class="title">
    <p class="title-kicker">COMMERCIAL&amp; INDUSTRIAL ELECTRICAL</p>
    <h1 class="title-main">MILLWRIGHT MAINTENANCE</h1>
    <div class="title-rule"></div>
  </header>

  <div class="badge">Services With over 100 years of experience on staff</div>

  <section class="services">
    <div class="service-block">
      <h2 class="service-title">Electrical &amp; Maintenance Services Locally or Nationwide <span class="hours">24/7</span></h2>
      <p class="service-copy">Summit Ridge Electrical Division provides electrical services for commercial and industrial clients. Certified and licensed electricians manage tasks such as automation, VFD and PLC control systems, wiring and motor repairs, cameras and communications cabling, including thermal imaging for annual inspections. The team is trained and experienced to complete electrical jobs safely and efficiently.</p>
    </div>
    <div class="service-block">
      <h2 class="service-title">Millwright &amp; MaintenanceServices Locally or Nationwide <span class="hours">24/7</span></h2>
      <p class="service-copy">We provide Millwright Maintenance and Industrial Rigging services. Our team is skilled in installing, maintaining, repairing, and troubleshooting industrial equipment.</p>
      <p class="service-copy">We handle turnkey projects as well as emergency repairs to ensure the efficient operation of factories or plants, from Project, Plant or Equipment Building Maintenance, on 24/7 call-out service.</p>
      <p class="service-copy">Additionally, we have a fabrication and welding shop for custom build of conveyors, equipment parts, and more.</p>
    </div>
  </section>

  <section class="industries">
    <h2 class="industries-head">Industries We Have<br>Experience Servicing</h2>
    <div class="industry-grid">
      <div class="industry"><div class="industry-photo tone-a" role="img" aria-label="Photo of a food and beverage production line"></div><span class="industry-label">Food &amp; Beverage</span></div>
      <div class="industry"><div class="industry-photo tone-b" role="img" aria-label="Photo of a pet food processing plant"></div><span class="industry-label">Pet Foods</span></div>
      <div class="industry"><div class="industry-photo tone-c" role="img" aria-label="Photo of industrial laundry machines"></div><span class="industry-label">Laundry Plants</span></div>
      <div class="industry"><div class="industry-photo tone-d" role="img" aria-label="Photo of grain silos and a flour mill"></div><span class="industry-label">Agriculture Grain &amp; Flour Mills</span></div>
      <div class="industry"><div class="industry-photo tone-c" role="img" aria-label="Photo of server racks in a data center"></div><span class="industry-label">Data Centers</span></div>
      <div class="industry"><div class="industry-photo tone-b" role="img" aria-label="Photo of a warehouse with storage racks"></div><span class="industry-label">Warehouse &amp; Distribution</span></div>
      <div class="industry"><div class="industry-photo tone-a" role="img" aria-label="Photo of a steel mill interior"></div><span class="industry-label">Steel Mills &amp; Processing Plants</span></div>
      <div class="industry"><div class="industry-photo tone-c" role="img" aria-label="Photo of water treatment tanks"></div><span class="industry-label">Water &amp; Wastewater</span></div>
      <div class="industry"><div class="industry-photo tone-d" role="img" aria-label="Photo of an oil field processing plant"></div><span class="industry-label">Oil Field &amp; Processing Plants</span></div>
      <div class="industry"><div class="industry-photo tone-b" role="img" aria-label="Photo of textile plant machinery"></div><span class="industry-label">Textile Plants</span></div>
    </div>
  </section>

  <div class="emergency">24 Hour Emergency Service call 555-014-2290 leave message.</div>

  <footer class="footer">
    <div class="contact">
      <svg viewBox="0 0 24 24" aria-hidden="true"><path d="M12 2a7 7 0 0 0-7 7c0 5 7 13 7 13s7-8 7-13a7 7 0 0 0-7-7zm0 9.5A2.5 2.5 0 1 1 12 6.5a2.5 2.5 0 0 1 0 5z" fill="#f5a623"/></svg>
      <p>Summit Ridge Millwrights &amp; Maintenance<br>1400 Granite Road, Unit 7<br>Denver, CO 80000</p>
    </div>
    <div class="contact">
      <svg viewBox="0 0 24 24" aria-hidden="true"><rect x="3" y="5" width="18" height="14" rx="2" fill="#f5a623"/><path d="M4 7l8 6 8-6" fill="none" stroke="#111" stroke-width="1.8"/></svg>
      <p>Office Email | office@summitridgemm.com</p>
    </div>
    <div class="contact">
      <svg viewBox="0 0 24 24" aria-hidden="true"><path d="M6.6 10.8a15 15 0 0 0 6.6 6.6l2.2-2.2a1 1 0 0 1 1-.25 11.4 11.4 0 0 0 3.6.57 1 1 0 0 1 1 1V20a1 1 0 0 1-1 1A17 17 0 0 1 3 4a1 1 0 0 1 1-1h3.5a1 1 0 0 1 1 1c0 1.25.2 2.45.57 3.6a1 1 0 0 1-.25 1z" fill="#f5a623"/></svg>
      <p>Main Office: 555-014-2290<br>Nick Vale - 555-014-3381<br>Dana Holt - 555-014-4472</p>
    </div>
  </footer>

</main>
</body>
</html>
```